The Green Sprout Website Design

I have hosting set up through Net Harbor but need Web Design for a new company called The Green Sprout. I am a holistic health coach helping individuals and groups achieve optimum health through the elimination of processed foods, GMOs, animal foods and chemical toxins in foods, beauty and household products and the promotion of a plant focused diet. I provide education and coaching programs to ensure success. The site should include my logo, the colors of black, white, orange and green and convey a simple, natural and friendly tone. My goal is to be a friendly resource to those who want or need to transition to a vegan lifestyle but don't want to feel judged or the need to be perfect to heal and make a difference. Progress vs perfection.

The tabs would be: Home About Services Recipes Resources (Things I Love) I.e affiliate links Contact Possibly a calendar of events As for products, they would be simple ebooks or 30 day programs delivered electronically. They are still in development. I will have a link to a free book excerpt for opting into my mailing list. You can see a site I built through my school's hosting for a basic example at Marisolkpenner.example While I like the basic bones of it, I wanted something more robust and not tied to the school.

```html
<!DOCTYPE html>
<html lang="en">
<head>
<meta charset="utf-8">
<title>The Green Sprout</title>
<link rel="stylesheet" href="https://fonts.googleapis.com/css2?family=Open+Sans:wght@300;400;600&display=swap">
<style>
  :root {
    --gold: #e2b044;
    --page: #f7f7f7;
    --white: #ffffff;
    --ink: #333333;
    --nav: #666666;
    --muted: #999999;
    --leaf: #6aa84f;
    --sun: #e8b53a;
    --accent: #8a5cd6;
    --hero-dark: #4a3d33;
    --hero-warm: #a8876a;
    --hero-apple: #c97a6a;
  }
  * { box-sizing: border-box; margin: 0; padding: 0; }
  html, body {
    width: 1200px; height: 675px; overflow: hidden;
    background: var(--page);
    font-family: "Open Sans", Arial, sans-serif;
    color: var(--ink);
  }
  .site {
    position: absolute; left: 145px; top: 0;
    width: 900px; height: 675px;
    background: var(--white);
    box-shadow: 0 0 8px rgba(0,0,0,0.12);
    overflow: hidden;
  }
  .topbar {
    height: 25px; background: var(--gold);
    display: flex; align-items: center;
    padding-left: 45px; gap: 10px;
    font-size: 10px; color: var(--white);
  }
  .topbar .contact { display: flex; align-items: center; gap: 3px; }
  .topbar .social { display: flex; gap: 13px; margin-left: 8px; }
  .topbar .social span {
    width: 8px; height: 8px; border-radius: 50%; background: var(--white); opacity: .85;
  }
  .header {
    height: 60px; display: flex; align-items: center;
    padding: 0 45px; justify-content: space-between;
  }
  .brand { display: flex; align-items: center; gap: 6px; font-size: 9.5px; color: var(--leaf); }
  .brand-dot { width: 26px; height: 26px; border-radius: 50%; border: 2px solid var(--sun); }
  .nav { display: flex; align-items: center; gap: 20px; font-size: 11.5px; color: var(--nav); }
  .nav .current { color: var(--ink); }
  .nav svg { margin-left: 6px; }
  .hero {
    position: relative; height: 500px;
    background:
      radial-gradient(ellipse at 75% 30%, rgba(220,150,120,.75), transparent 55%),
      radial-gradient(ellipse at 50% 95%, rgba(215,130,110,.8), transparent 60%),
      linear-gradient(160deg, var(--hero-dark) 0%, #6b5a4b 45%, var(--hero-warm) 75%, var(--hero-apple) 100%);
    text-align: center; color: var(--white);
  }
  .hero-text { position: absolute; left: 0; right: 0; top: 150px; }
  .hero h1 { font-weight: 300; font-size: 36px; line-height: 50px; }
  .hero p {
    width: 650px; margin: 0 auto; font-size: 13.5px; line-height: 22px;
    text-shadow: 0 1px 3px rgba(0,0,0,.4);
  }
  .hero .button {
    display: inline-block; margin-top: 14px;
    border: 2px solid var(--white); border-radius: 3px;
    padding: 5px 14px; font-size: 15px;
  }
  .dots { position: absolute; bottom: 26px; left: 0; right: 0; display: flex; justify-content: center; gap: 7px; }
  .dots span { width: 6px; height: 6px; border-radius: 50%; background: rgba(255,255,255,.5); }
  .dots .active { background: var(--white); }
  .features { display: flex; padding: 57px 45px 0; }
  .feature { width: 285px; flex-shrink: 0; display: flex; gap: 15px; }
  .feature h3 { font-weight: 400; font-size: 14px; line-height: 20px; color: var(--ink); }
  .feature p { font-size: 10.5px; color: var(--muted); white-space: nowrap; }
</style>
</head>
<body>
<div class="site">
  <div class="topbar">
    <span class="contact">
      <svg width="9" height="9" viewBox="0 0 10 10"><path d="M2 1l2 2-1 1.5c.8 1.4 1.6 2.2 3 3L7.5 6l2 2-1.5 1.5C4.5 9 1 5.5.5 2z" fill="#fff"/></svg>555-0148
    </span>
    <span class="contact">
      <svg width="10" height="8" viewBox="0 0 10 8"><rect width="10" height="8" fill="#fff"/><path d="M0 0l5 4 5-4" stroke="#e2b044" fill="none"/></svg>hello@greensprout.example
    </span>
    <span class="social"><span></span><span></span><span></span><span></span></span>
  </div>
  <header class="header">
    <div class="brand"><span class="brand-dot"></span>The Green Sprout</div>
    <nav class="nav">
      <span class="current">Home</span><span>Services</span><span>Recipes</span><span>Resources</span><span>About</span>
      <svg width="12" height="12" viewBox="0 0 12 12"><circle cx="5" cy="5" r="4" stroke="#777" fill="none" stroke-width="1.3"/><path d="M8 8l3.5 3.5" stroke="#777" stroke-width="1.3"/></svg>
    </nav>
  </header>
  <section class="hero" role="img" aria-label="Photo of fresh sliced and whole red-yellow apples in a bowl and a cardboard box on a wooden table">
    <div class="hero-text">
      <h1>Welcome To Our Website</h1>
      <p>Vivamus ipsum velit, ullamcorper quis nibh non, molestie tempus sapien. Mauris ultrices, felis ut eleifend auctor, leo felis vehicula quam, ut accumsan augue nunc at nisl. Cras venenatis ac lorema ac tincidunt. Mauris ultrices, felis ut eleifend auctor, leo felis vehicula quam, ut accumsan augue.</p>
      <span class="button">Learn More</span>
    </div>
    <div class="dots"><span></span><span class="active"></span><span></span></div>
  </section>
  <section class="features">
    <div class="feature">
      <svg width="24" height="22" viewBox="0 0 24 22"><rect x="1" y="1" width="22" height="20" fill="none" stroke="#8a5cd6" stroke-width="2"/><circle cx="15" cy="7" r="2.5" fill="#8a5cd6"/><path d="M3 19l6-8 4 5 3-3 5 6z" fill="#8a5cd6"/></svg>
      <div><h3>Feature 1</h3><p>Vestibulum lobortis. Donec at euismod</p></div>
    </div>
    <div class="feature">
      <svg width="24" height="22" viewBox="0 0 24 22"><rect x="1" y="1" width="22" height="20" fill="none" stroke="#8a5cd6" stroke-width="2"/><circle cx="15" cy="7" r="2.5" fill="#8a5cd6"/><path d="M3 19l6-8 4 5 3-3 5 6z" fill="#8a5cd6"/></svg>
      <div><h3>Feature 2</h3><p>Vestibulum lobortis. Donec at euismod</p></div>
    </div>
    <div class="feature">
      <svg width="24" height="22" viewBox="0 0 24 22"><rect x="1" y="1" width="22" height="20" fill="none" stroke="#8a5cd6" stroke-width="2"/><circle cx="15" cy="7" r="2.5" fill="#8a5cd6"/><path d="M3 19l6-8 4 5 3-3 5 6z" fill="#8a5cd6"/></svg>
      <div><h3>Feature 3</h3><p>Vestibulum lobortis. Donec at euismod</p></div>
    </div>
  </section>
</div>
</body>
</html>
```